Sex Trafficked women Empowered Business Card Design Project

I would like a two-sided business card. On the front, please include: Marta Oberlin, Executive Director 555-284-7316, www.tallowcrest.org, marta@tallowcrest.org and logo.

On the back:
Vision
Survivors of sexual exploitation live free, fulfilling their God-given purpose.

Perhaps a QR code to direct them to the website: www.tallowcrest.org

I want to try a deeper color for the logo. i have added these files.

My desire is to communicate hope, freedom and new life.
Updates

i decided to ask for business card designs with a deeper toned logo. see new files attached

i have placed the vertical logo as an option, but i would still want the logo with tagline used.

Target Market(s)

I want a professional look to appeal to donors who have a heart to help sexually exploited women. I chose a logo that was light enough to look good on a variety of backgrounds. I do want the logo to catch attention.

Industry/Entity Type

Business

Font styles to use
Serif

Requirements
Must have
• i want to be able to read the tagline. Also, the design should match the look and feel of the logo.

Nice to have
• Since there isn't much text on the back, feel free to be a bit more creative. I still want a professional look.

```html
<!DOCTYPE html>
<html lang="en">
<head>
<meta charset="utf-8">
<title>Tallowcrest – Business Card</title>
<link rel="stylesheet" href="https://fonts.googleapis.com/css2?family=Questrial&family=Tinos:wght@400;700&display=swap">
<style>
  :root {
    --band-red: #8e2a27;
    --ink: #1a1a1a;
    --paper-light: #ffffff;
    --paper-edge: #c4c4c4;
    --mark-blue: #2a6db5;
    --band-text: #ffffff;
  }
  html, body {
    margin: 0;
    padding: 0;
    width: 1200px;
    height: 703px;
    overflow: hidden;
    background: #ffffff;
  }
  .card {
    position: relative;
    width: 1200px;
    height: 703px;
    overflow: hidden;
    background: radial-gradient(ellipse 70% 75% at 45% 50%, var(--paper-light) 0%, #ececec 55%, var(--paper-edge) 100%);
    font-family: "Tinos", "Times New Roman", serif;
    color: var(--ink);
  }
  .band {
    position: absolute;
    left: 0;
    width: 100%;
    background: var(--band-red);
  }
  .band--top { top: 46px; height: 58px; }
  .band--bottom {
    top: 590px;
    height: 64px;
    display: flex;
    align-items: center;
    justify-content: center;
  }
  .website {
    color: var(--band-text);
    font-size: 36px;
    letter-spacing: 8px;
  }
  .brand {
    position: absolute;
    left: 690px;
    top: 130px;
    display: flex;
    align-items: center;
    gap: 26px;
  }
  .brand__dot {
    width: 104px;
    height: 104px;
    border-radius: 50%;
    background: var(--mark-blue);
  }
  .brand__name {
    font-size: 50px;
    font-weight: 700;
    color: var(--ink);
  }
  .person {
    position: absolute;
    left: 62px;
    top: 272px;
    font-family: "Questrial", "Century Gothic", sans-serif;
  }
  .person__name {
    margin: 0;
    font-weight: 400;
    font-size: 62px;
    line-height: 1;
    letter-spacing: 1px;
  }
  .person__initial { font-size: 84px; }
  .person__title {
    margin: 6px 0 0;
    text-align: right;
    font-size: 27px;
  }
  .contact {
    position: absolute;
    left: 780px;
    top: 452px;
    font-size: 28px;
    line-height: 50px;
  }
  .contact p { margin: 0; }
</style>
</head>
<body>
  <main class="card">
    <div class="band band--top"></div>

    <div class="brand">
      <div class="brand__dot"></div>
      <span class="brand__name">Tallowcrest</span>
    </div>

    <section class="person">
      <h1 class="person__name"><span class="person__initial">M</span>arta <span class="person__initial">O</span>berlin</h1>
      <p class="person__title">Executive Director</p>
    </section>

    <section class="contact">
      <p>555-284-7316 Phone</p>
      <p>E-mail marta@tallowcrest.org</p>
    </section>

    <div class="band band--bottom">
      <span class="website">www.tallowcrest.org</span>
    </div>
  </main>
</body>
</html>
```